Glossaro: Graphic elements & webpage layout

Hi there! We’re building a site called Glossaro.com—it will be a community site for beauty product reviews, product recommendations and beauty tutorials. We've already got a logo, thanks to another ArtHively project. This project on ArtHively involves the following web design work:

1) Propose the overall graphic design elements of our site (according to our guidelines, which are in the attached file)

-Color Palette
-Fonts
-Icon set(s)

2) Using the overall graphic design elements in step 1 and our storyboard (attached), develop a webpage layout for the "How-to" page of our site. The "How-to" pages will be an editorial format, where our beauty journalist will show a video (and photos) of step-by-step beauty tutorials.

Please take a look at the attached files for a detailed brief and the logo! Thanks and we're looking forward to working with you!

Target Market(s)

Glossaro is for a French, English, and American audience of women between the ages of 16 and 30, who buy and use beauty products regularly.

Industry/Entity Type

Graphic Design

Requirements
Must have
• 1) A global set of graphic standards for the website Glossaro.com:
• A color palette
• Fonts
• An icon set (or sets)
• A menu
• Other graphic elements like button styles

2) A webpage layout (non-coded) for the How-To page template
(See storyboard, attached separately)
This webpage layout is for the main editorial format on Glossaro—step by step beauty tutorials. The individual on-page elements are in the storyboard, but overall we’d like it to look clean, friendly, and to encourage community participation and sharing on social networks.
Nice to have
• • A look and feel that is fresh, clean and modern
• Proximity: Establishes a close proximity with the user. (We want them to get the same feeling they get when talking beauty tips with their close friends).
• Neutrality: A sincere and neutral look and feel that doesn’t suggest a preference for any particular or elite type of beauty (but it can still be fun!)
• The graphic design is relevant to the beauty sector as a whole. (We could be talking about lipstick, a hairbrush or a man’s cologne)
• The graphic design alludes to the beauty industry (discreetly, not overtly!)
Should not have
• We've already got a logo, so you shouldn't suggest a new one!

We really want to avoid designs that are too traditionally "beauty" or too girly and feminine. Please no pink, no flowers, etc! :)

```html
<!DOCTYPE html>
<html lang="fr">
<head>
<meta charset="utf-8">
<title>Glossaro – Tutorial</title>
<link href="https://fonts.googleapis.com/css2?family=Signika:wght@400;600&family=Open+Sans:wght@400;600&display=swap" rel="stylesheet">
<style>
:root{
  --page-olive:#c3cd92;
  --column:#eef1dd;
  --header-band:#e3f5d3;
  --green:#5f9a2c;
  --green-btn:#6aaa2e;
  --teal:#1d9aa8;
  --teal-dark:#13808d;
  --ink:#2c2c2c;
  --muted:#555;
  --line:#c9d6b8;
  --footer:#2a2a2a;
  --panel:#f6f8ee;
}
*{box-sizing:border-box;margin:0;padding:0}
html,body{width:749px;height:1200px;overflow:hidden}
body{background:var(--page-olive);font-family:"Open Sans",Arial,sans-serif;color:var(--ink);position:relative}
.column{position:absolute;left:118px;top:0;width:512px;height:1155px;background:var(--column)}
.topbar{position:absolute;top:5px;right:124px;display:flex;gap:6px}
.flag,.social-mini{width:15px;height:13px;border-radius:2px}
.flag-uk{background:#243f8f;position:relative;overflow:hidden}
.flag-uk::before{content:"";position:absolute;left:6px;top:0;width:3px;height:13px;background:#fff;box-shadow:0 0 0 1px #d22}
.flag-uk::after{content:"";position:absolute;top:5px;left:0;height:3px;width:15px;background:#d22}
.flag-fr{background:linear-gradient(90deg,#23408f 33%,#fff 33% 66%,#d22 66%)}
.social-mini{background:#3b5a9a;border-radius:3px}
.social-mini.alt{background:#2aa8c8}
.header{position:absolute;left:0;top:25px;width:749px;height:72px;background:var(--header-band);border-top:1px solid #fff;border-bottom:1px solid #d6e3c4}
.brand{position:absolute;left:124px;top:14px;display:flex;align-items:center;gap:6px;font-family:"Signika",sans-serif;font-weight:600;font-size:34px;color:var(--ink);letter-spacing:-0.5px}
.brand-dot{width:12px;height:12px;border-radius:50%;background:var(--teal)}
.nav{position:absolute;left:329px;top:29px;display:flex;font-family:"Signika",sans-serif;font-size:11px;color:var(--ink)}
.nav a{color:inherit;text-decoration:none;padding:0 8px;border-left:1px solid #555;line-height:13px}
.nav a:first-child{border-left:0;padding-left:0}
.search{position:absolute;left:495px;top:27px;width:130px;height:18px;border:1px solid #c8d7b4;border-radius:10px;background:#eef7e4;font-size:7px;color:#444;padding:4px 8px}
.search svg{position:absolute;right:6px;top:3px}
.title{position:absolute;left:122px;top:115px;font-family:"Signika",sans-serif;font-size:22px;color:var(--green);font-weight:400}
.share{position:absolute;left:556px;top:120px;display:flex;gap:7px}
.share span{width:19px;height:19px;border-radius:4px;background:#3b5a9a}
.share span:nth-child(2){background:#3fb1dc}
.share span:nth-child(3){background:#f07b20}
.meta{position:absolute;top:148px;left:122px;width:340px;font-family:"Signika",sans-serif;font-size:10px;color:var(--ink);display:flex}
.meta b{font-weight:400;color:var(--teal);font-size:13px}
.meta .diff{width:115px;display:flex;align-items:center;gap:4px}
.meta .dur{width:133px}
.leaf{display:inline-block;width:4px;height:11px;background:var(--teal);border-radius:3px;transform:skewX(-30deg);margin-left:2px}
.media{position:absolute;left:122px;width:336px;background:#fff;border:1px solid #d3d8c8}
.media-fill{position:absolute;left:0;top:0;right:0;bottom:10px}
.controls{position:absolute;left:0;right:0;bottom:0;height:10px;background:#eee;border-top:1px solid #ccc;font-size:5px;display:flex;align-items:center;padding:0 3px;gap:3px}
.controls .track{flex:1;height:2px;background:#bbb}
.play{position:absolute;width:28px;height:28px;border-radius:4px;background:rgba(200,200,200,.8);display:flex;align-items:center;justify-content:center}
.sidebar{position:absolute;left:465px;top:166px;width:162px;height:192px;background:var(--panel);border:1px solid #cfd9be}
.sidebar h3{background:var(--teal);color:#fff;font-family:"Signika",sans-serif;font-weight:400;font-size:9px;letter-spacing:.4px;padding:5px 7px;height:20px}
.sidebar ul{list-style:none;padding:3px 6px 0}
.sidebar li{font-size:7px;color:#555;height:15.8px;line-height:15px;border-bottom:1px dotted var(--line);padding-left:12px;position:relative}
.sidebar li::before,.arrow-mark::before{content:"";position:absolute;left:1px;top:6px;width:7px;height:3px;border-radius:2px;background:var(--teal)}
.view-all{font-size:7px;color:var(--teal);text-align:right;padding-right:9px}
.sidebar .view-all{margin-top:4px}
.text{position:absolute;left:122px;width:336px;font-size:6.4px;line-height:8.4px;color:#333}
.step{position:absolute;left:122px;font-family:"Signika",sans-serif;font-size:13px;color:var(--green)}
.step::before{content:"";display:inline-block;width:9px;height:3px;border-radius:2px;background:var(--green);vertical-align:middle;margin-right:5px}
.tabs{position:absolute;left:127px;display:flex;gap:3px}
.tab{width:60px;height:17px;border-radius:6px 6px 0 0;background:var(--footer);color:#fff;font-family:"Signika",sans-serif;font-size:10px;text-align:center;line-height:18px}
.tab.on-green{background:var(--green-btn)}
.tab.on-teal{background:var(--teal)}
.products{position:absolute;left:465px;width:162px;height:189px;background:var(--panel);border:1px solid #cfd9be}
.prod{position:absolute;width:78px;height:44px}
.thumb{position:absolute;left:0;top:0;width:39px;height:42px;border:1px solid #bbb}
.info{position:absolute;left:42px;top:0;font-size:6px;line-height:8.5px;color:#666}
.buy{position:absolute;left:41px;top:33px;width:35px;height:10px;border-radius:3px;background:var(--green-btn);color:#fff;font-size:6px;line-height:10px;text-align:right;padding-right:3px}
.buy::before{content:"";position:absolute;left:3px;top:3px;width:5px;height:4px;border:1px solid #fff;border-top:0;border-radius:0 0 1px 1px}
.buy.teal{background:var(--teal)}
.products .view-all{position:absolute;right:0;bottom:5px}
.slider-btn{position:absolute;top:76px;width:28px;height:27px;border-radius:6px;background:rgba(60,60,60,.75);display:flex;align-items:center;justify-content:center}
.plugin-label{position:absolute;left:126px;top:1020px;font-size:6.5px;color:#555;display:flex;align-items:center;gap:4px}
.sq{width:9px;height:9px;background:#3b5a9a;border-radius:1px}
.avatar{position:absolute;left:126px;top:1040px;width:34px;height:35px;background:linear-gradient(#9a9a9a,#d5d5d5);border:1px solid #aaa}
.comment-box{position:absolute;left:165px;top:1042px;width:294px;height:81px;border:1px solid #c8ceba;background:#eef1e2}
.comment-box .who{position:absolute;left:8px;top:5px;font-size:7px;display:flex;gap:4px;align-items:center}
.comment-box .field{position:absolute;left:7px;top:18px;width:280px;height:35px;background:#fff;border:1px solid #bbb;font-size:7px;color:#888;padding:3px}
.comment-box .opts{position:absolute;right:8px;top:60px;display:flex;align-items:center;gap:5px;font-size:7px;color:#333}
.tick{width:8px;height:8px;border:1px solid #667}
.post{background:#5a74ae;color:#fff;font-weight:600;padding:2px 5px;border:1px solid #3b5a9a}
.admin{position:absolute;left:375px;top:1126px;font-size:7px;color:#3b5a9a}
.footer{position:absolute;left:0;top:1155px;width:749px;height:45px;background:var(--footer)}
.footer p{position:absolute;left:122px;top:8px;width:380px;font-size:5.4px;line-height:8.6px;color:#ddd}
.footer .brand-small{position:absolute;left:556px;top:7px;font-family:"Signika",sans-serif;font-weight:600;font-size:17px;color:#fff}
.footer .year{position:absolute;left:587px;top:30px;font-size:5px;color:#ddd}
</style>
</head>
<body>
<div class="column"></div>

<div class="topbar">
  <span class="flag flag-uk" aria-label="English"></span>
  <span class="flag flag-fr" aria-label="Français"></span>
  <span class="social-mini"></span>
  <span class="social-mini alt"></span>
</div>

<header class="header">
  <div class="brand"><span>Glossaro</span><span class="brand-dot"></span></div>
  <nav class="nav"><a href="#">How To</a><a href="#">TIPS</a><a href="#">Nav 1</a><a href="#">Nav 2</a></nav>
  <div class="search">Search...
    <svg width="14" height="11" viewBox="0 0 14 11"><circle cx="5" cy="5" r="4" fill="none" stroke="#1d9aa8" stroke-width="1.5"/><line x1="8" y1="8" x2="13" y2="10" stroke="#1d9aa8" stroke-width="1.5"/></svg>
  </div>
</header>

<h1 class="title">[TITRE DU TUTORIAL]</h1>
<div class="share"><span></span><span></span><span></span></div>

<div class="meta">
  <div class="diff">Difficulté: <span class="leaf"></span><span class="leaf"></span><span class="leaf"></span></div>
  <div class="dur">Durée: <b>20 minutes</b></div>
  <div>Occasion: <b>Soirée</b></div>
</div>

<div class="media" style="top:166px;height:189px">
  <div class="media-fill" role="img" aria-label="Tutorial video still: facial care scene" style="background:linear-gradient(120deg,#e9d9cd,#f4ece6 50%,#c9a98f)"></div>
  <div class="play" style="left:153px;top:77px"><svg width="10" height="12"><path d="M0 0L10 6L0 12Z" fill="#111"/></svg></div>
  <div class="controls"><span>❚❚</span><span>00:00</span><span class="track"></span><span>00:00</span></div>
</div>

<aside class="sidebar">
  <h3>LES PRODUITS NÉCESSAIRES</h3>
  <ul>
    <li>Produit 1</li><li>Produit 2</li><li>Produit 3</li><li>Produit 4</li><li>Produit 5</li>
    <li>Produit 6</li><li>Produit 7</li><li>Produit 8</li><li>Produit 9</li><li>Produit 10</li>
  </ul>
  <div class="view-all">+ View All Produit</div>
</aside>

<p class="text" style="top:366px">Lorem ipsum dolor sit amet, maiores ornare ac fermentum, imperdiet ut vivamus a, nam lectus at nunc. Quam euismod sem, semper ut potenti pellentesque quisque. In eget sapien sed, sit duis vestibulum ultricies, placerat morbi amet vel, nullam in in lorem vel.</p>

<h2 class="step" style="top:408px">ETAPE 1</h2>
<div class="tabs" style="top:441px"><div class="tab on-green">Vidéo</div><div class="tab">Photos</div></div>

<div class="media" style="top:458px;height:189px">
  <div class="media-fill" role="img" aria-label="Tutorial video still: lips, nail and eye makeup illustrations" style="left:55px;top:16px;bottom:39px;background:linear-gradient(90deg,#f0a98a,#f7f3f2 45%,#f3c2a8)"></div>
  <div class="play" style="left:153px;top:75px"><svg width="10" height="12"><path d="M0 0L10 6L0 12Z" fill="#111"/></svg></div>
  <div class="controls"><span>❚❚</span><span>00:00</span><span class="track"></span><span>00:00</span></div>
</div>

<div class="products" style="top:458px">
  <div class="prod" style="left:3px;top:3px"><div class="thumb" role="img" aria-label="Lipstick product photo" style="background:linear-gradient(#fff,#e33 70%)"></div><div class="info">Produit 1<br>Marque<br>Prix</div><span class="buy">Acheter</span></div>
  <div class="prod" style="left:83px;top:3px"><div class="thumb" role="img" aria-label="Cream jar product photo" style="background:linear-gradient(#f4e8ee,#d8527f)"></div><div class="info">Produit 1<br>Marque<br>Prix</div><span class="buy teal">Acheter</span></div>
  <div class="prod" style="left:3px;top:64px"><div class="thumb" role="img" aria-label="Bottles product photo" style="background:linear-gradient(#fff,#ccc)"></div><div class="info">Produit 1<br>Marque<br>Prix</div><span class="buy">Acheter</span></div>
  <div class="prod" style="left:83px;top:64px"><div class="thumb" role="img" aria-label="Skincare set product photo" style="background:linear-gradient(#cfe9ee,#9dd0b8)"></div><div class="info">Produit 1<br>Marque<br>Prix</div><span class="buy teal">Acheter</span></div>
  <div class="prod" style="left:3px;top:124px"><div class="thumb" role="img" aria-label="Lip gloss product photo" style="background:linear-gradient(90deg,#222,#f2a7b5)"></div><div class="info">Produit 1<br>Marque<br>Prix</div><span class="buy">Acheter</span></div>
  <div class="prod" style="left:83px;top:124px"><div class="thumb" role="img" aria-label="Red lipstick product photo" style="background:linear-gradient(90deg,#c1121a,#f5f5f5)"></div><div class="info">Produit 1<br>Marque<br>Prix</div><span class="buy teal">Acheter</span></div>
  <div class="view-all">+ View All</div>
</div>

<p class="text" style="top:657px">Lorem ipsum dolor sit amet, maiores ornare ac fermentum, imperdiet ut vivamus a, nam lectus at nunc. Quam euismod sem, semper ut potenti pellentesque quisque. In eget sapien sed, sit duis vestibulum ultricies, placerat morbi amet vel, nullam in in lorem vel.</p>

<h2 class="step" style="top:705px">ETAPE 2</h2>
<div class="tabs" style="top:735px"><div class="tab">Vidéo</div><div class="tab on-teal">Photos</div></div>

<div class="media" style="top:752px;height:188px">
  <div class="media-fill" role="img" aria-label="Step photo: skincare product beside a portrait" style="bottom:0;background:linear-gradient(90deg,#3a2a22,#c8a892 28%,#f4f6f7 45%,#e6eef0)"></div>
  <div class="slider-btn" style="left:3px"><svg width="10" height="14"><path d="M8 1L2 7L8 13" fill="none" stroke="#fff" stroke-width="3"/></svg></div>
  <div class="slider-btn" style="right:3px"><svg width="10" height="14"><path d="M2 1L8 7L2 13" fill="none" stroke="#111" stroke-width="3"/></svg></div>
</div>

<div class="products" style="top:752px">
  <div class="prod" style="left:3px;top:3px"><div class="thumb" role="img" aria-label="Lipstick product photo" style="background:linear-gradient(#fff,#e33 70%)"></div><div class="info">Produit 1<br>Marque<br>Prix</div><span class="buy">Acheter</span></div>
  <div class="prod" style="left:83px;top:3px"><div class="thumb" role="img" aria-label="Cream jar product photo" style="background:linear-gradient(#f4e8ee,#d8527f)"></div><div class="info">Produit 1<br>Marque<br>Prix</div><span class="buy teal">Acheter</span></div>
  <div class="prod" style="left:3px;top:64px"><div class="thumb" role="img" aria-label="Bottles product photo" style="background:linear-gradient(#fff,#ccc)"></div><div class="info">Produit 1<br>Marque<br>Prix</div><span class="buy">Acheter</span></div>
  <div class="prod" style="left:83px;top:64px"><div class="thumb" role="img" aria-label="Skincare set product photo" style="background:linear-gradient(#cfe9ee,#9dd0b8)"></div><div class="info">Produit 1<br>Marque<br>Prix</div><span class="buy teal">Acheter</span></div>
  <div class="prod" style="left:3px;top:124px"><div class="thumb" role="img" aria-label="Lip gloss product photo" style="background:linear-gradient(90deg,#222,#f2a7b5)"></div><div class="info">Produit 1<br>Marque<br>Prix</div><span class="buy">Acheter</span></div>
  <div class="prod" style="left:83px;top:124px"><div class="thumb" role="img" aria-label="Red lipstick product photo" style="background:linear-gradient(90deg,#c1121a,#f5f5f5)"></div><div class="info">Produit 1<br>Marque<br>Prix</div><span class="buy teal">Acheter</span></div>
  <div class="view-all">+ View All</div>
</div>

<p class="text" style="top:951px">Lorem ipsum dolor sit amet, maiores ornare ac fermentum, imperdiet ut vivamus a, nam lectus at nunc. Quam euismod sem, semper ut potenti pellentesque quisque. In eget sapien sed, sit duis vestibulum ultricies, placerat morbi amet vel, nullam in in lorem vel.</p>

<h2 class="step" style="top:993px">COMMENTAIRES (12)</h2>
<div class="plugin-label"><span class="sq"></span>Socialine social plugin</div>

<div class="avatar" role="img" aria-label="User profile photo"></div>
<div class="comment-box">
  <div class="who"><span class="sq"></span>Logged in as</div>
  <div class="field">Add a comment...</div>
  <div class="opts"><span class="tick"></span><span>Post comment to my Socialine profile</span><span class="post">Post</span></div>
</div>
<div class="admin">Administer Comments</div>

<footer class="footer">
  <p>Lorem ipsum dolor sit amet, maiores ornare ac fermentum, imperdiet ut vivamus a, nam lectus at nunc. Quam euismod sem, semper ut potenti pellentesque quisque. In eget sapien sed, sit duis vestibulum ultricies, placerat morbi amet vel, nullam in in lorem vel.<br>Commentaire de [nom] posté le [date]</p>
  <div class="brand-small">Glossaro</div>
  <div class="year">© 2011</div>
</footer>
</body>
</html>
```